Windshield wiper website

I have a website through hostmarlo.com named Bravoblades.com
I'm looking to include the windshield wiper sizes needed for vehicles in a user-friendly format. Along with a page to order the wipers from. I supply all the wiper blades in sizes 14,16,17,18,19,20,21,22,24,26,28,30, and 32"
The wiper blades are silicone beam blade.
Our motto is 'see it clearly'
I've tried designing a website already at bravoblades.com but I feel like it doesn't look legit enough to acquire sales.

Target Market(s)

Every vehicle in the USA.

Industry/Entity Type

Auto parts - New

Coding

Coded - Design and coding required

Number of Pages Required

5+ page

Font styles to use
Sans Serif

Requirements
Must have
• User friendly way to find out what size windshield wiper they need for their specific vehicle.
Nice to have
• A way to automatically email a purchaser one year after a sale to get a repeat customer.

```html
<!DOCTYPE html>
<html lang="en">
<head>
<meta charset="utf-8">
<title>Bravo Blades — See It Clearly</title>
<link href="https://fonts.googleapis.com/css2?family=Josefin+Sans:wght@400;600;700&family=Lato:wght@400;700&display=swap" rel="stylesheet">
<style>
:root{
  --orange:#f7731f;
  --orange-dark:#e8620f;
  --ink:#222222;
  --text:#3b3b3b;
  --muted:#7a7a7a;
  --panel:#f2f2f2;
  --white:#ffffff;
  --section-dark:#4b4b4e;
  --footer:#58585b;
}
*{box-sizing:border-box;margin:0;padding:0}
html,body{width:1200px;height:3727px;overflow:hidden}
body{position:relative;background:var(--white);font-family:'Lato',sans-serif;color:var(--text)}
.abs{position:absolute}
.head{font-family:'Josefin Sans',sans-serif;font-weight:700;color:var(--ink)}
.btn{position:absolute;background:var(--orange);color:var(--white);font-family:'Lato',sans-serif;font-weight:700;font-size:15px;display:flex;align-items:center;justify-content:center;border-radius:6px;box-shadow:0 8px 16px rgba(247,115,31,.35);letter-spacing:.3px}

/* header */
.site-header{left:0;top:0;width:1200px;height:104px;background:var(--white)}
.brand{left:155px;top:38px;font-family:'Lato',sans-serif;font-weight:700;font-size:23px;letter-spacing:1.5px;color:var(--ink)}
.nav a{position:absolute;top:43px;font-size:14px;color:var(--ink);text-decoration:none}
.search{left:730px;top:32px;width:227px;height:38px;border:1px solid #cfcfcf;border-radius:20px;font-size:13px;color:#9a9a9a;padding:11px 14px}
.search-btn{left:925px;top:34px;width:32px;height:34px;border-radius:50%;border:1px solid #cfcfcf;display:flex;align-items:center;justify-content:center}
.cart-badge{left:1023px;top:32px;width:15px;height:15px;border-radius:50%;background:var(--orange);color:#fff;font-size:9px;display:flex;align-items:center;justify-content:center}

/* hero */
.hero{left:0;top:104px;width:1200px;height:665px;background:linear-gradient(180deg,#c98a3c 0%,#e0a24c 22%,#8a6a45 45%,#4c443d 70%,#2e2c2b 100%)}
.finder{left:91px;top:223px;width:371px;height:414px;background:rgba(255,255,255,.55);border-radius:6px}
.finder h2{position:absolute;left:0;width:100%;top:36px;text-align:center;font-family:'Josefin Sans',sans-serif;font-weight:700;font-size:21px;letter-spacing:1px;color:var(--ink)}
.select{position:absolute;left:29px;width:311px;height:44px;background:var(--white);border-radius:5px;font-size:13px;color:#888;padding:14px 14px}
.select::after{content:"";position:absolute;right:16px;top:19px;border:5px solid transparent;border-top:6px solid #222}
.select.first{color:var(--ink)}
.finder .btn{left:29px;top:306px;width:311px;height:46px;font-size:14px}
.help{position:absolute;left:0;width:100%;top:373px;text-align:center;font-size:13px;color:var(--ink)}
.help u{text-decoration:underline}
.hero-title{left:525px;top:290px;font-family:'Josefin Sans',sans-serif;font-weight:700;color:var(--white);font-size:54px;line-height:60px;letter-spacing:1.5px}

/* welcome */
.welcome-title{left:149px;top:868px;font-size:48px;line-height:54px;letter-spacing:1.5px}
.welcome-copy{left:149px;top:991px;width:510px;font-size:15px;line-height:19.5px;color:var(--text)}
.welcome-copy p+p{margin-top:19px}
.ring{left:685px;top:877px;width:363px;height:363px;border-radius:50%;border:2px solid var(--ink)}
.ring-photo{left:702px;top:894px;width:329px;height:329px;border-radius:50%;background:radial-gradient(circle at 50% 40%,#d4dde3 0%,#9fb0ba 55%,#2b2f33 100%)}

/* wipers */
.wipers{left:0;top:1358px;width:1200px;height:628px;background:linear-gradient(90deg,#3f3f42 0%,#5a5a5d 50%,#3f3f42 100%)}
.wipers-title{left:0;width:1200px;top:1425px;text-align:center;font-size:46px;color:var(--white);letter-spacing:1.5px}
.wipers-sub{left:0;width:1200px;top:1482px;text-align:center;font-family:'Josefin Sans',sans-serif;font-weight:600;font-size:18px;letter-spacing:1px;color:#e6e6e6}
.wipers-sub em{color:var(--orange);font-style:italic;font-weight:700}
.product{position:absolute;top:1549px;width:282px;height:289px}
.product-photo{position:absolute;left:0;top:0;width:282px;height:232px;border:2px solid #ddd;border-radius:6px 6px 0 0;background:linear-gradient(180deg,#b9bcbe 0%,#9a9ea1 45%,#7f8386 100%)}
.product-tag{position:absolute;left:16px;top:195px;width:252px;height:94px;background:var(--white);border-radius:6px;text-align:center;padding-top:14px}
.product-tag .name{font-family:'Josefin Sans',sans-serif;font-size:14px;line-height:15px;color:#444}
.product-tag .meta{margin-top:14px;font-family:'Josefin Sans',sans-serif;font-size:13px;color:#888}
.product-tag .price{font-family:'Lato',sans-serif;font-weight:700;font-size:16px;color:var(--ink);margin-left:18px}
.arrow{position:absolute;top:1628px}

/* features */
.feat-photo{position:absolute;width:514px;height:316px}
.feat-box{position:absolute;background:var(--panel);padding:36px 50px 0 49px}
.feat-box h3{font-family:'Josefin Sans',sans-serif;font-weight:700;font-size:29px;color:var(--ink);margin-bottom:16px}
.feat-box p{font-size:15px;line-height:19.5px;color:var(--text)}
.feat-box p+p{margin-top:19px}

/* footer */
.footer{left:0;top:3307px;width:1200px;height:420px;background:linear-gradient(180deg,#4d4d50 0%,#626265 55%,#55555a 100%)}
.f-head{position:absolute;top:3412px;font-family:'Josefin Sans',sans-serif;font-weight:700;font-size:22px;letter-spacing:.8px;color:var(--white)}
.f-list{position:absolute;top:3457px;font-size:14px;line-height:29px;color:#f0f0f0;list-style:none}
.divider{left:560px;top:3409px;width:1px;height:149px;background:#9a9a9d}
.f-note{left:661px;top:3457px;width:390px;font-size:13px;line-height:17px;color:#f0f0f0}
.email{left:659px;top:3514px;width:300px;height:44px;background:var(--white);border-radius:5px 0 0 5px;font-size:13px;color:#333;padding:14px 14px}
.copyright{left:0;width:1200px;top:3665px;text-align:center;font-size:13px;color:#f0f0f0}
</style>
</head>
<body>

<header class="abs site-header">
  <div class="abs brand">BRAVO BLADES</div>
  <nav class="nav">
    <a style="left:348px">Home</a>
    <a style="left:434px">Contact Us</a>
    <a style="left:552px">About Us</a>
    <a style="left:659px">Order</a>
  </nav>
  <div class="abs search">Enter Keyword</div>
  <div class="abs search-btn">
    <svg width="13" height="13" viewBox="0 0 13 13"><circle cx="5.5" cy="5.5" r="4" fill="none" stroke="#222" stroke-width="1.8"/><line x1="8.5" y1="8.5" x2="12" y2="12" stroke="#222" stroke-width="1.8"/></svg>
  </div>
  <svg class="abs" style="left:969px;top:37px" width="24" height="26" viewBox="0 0 24 26"><circle cx="12" cy="7" r="5.5" fill="none" stroke="#222" stroke-width="1.8"/><path d="M2 25c0-6 4.5-9 10-9s10 3 10 9" fill="none" stroke="#222" stroke-width="1.8"/></svg>
  <svg class="abs" style="left:1003px;top:38px" width="30" height="27" viewBox="0 0 30 27"><path d="M1 2h5l4 15h15l3-11H8" fill="none" stroke="#222" stroke-width="1.8" stroke-linejoin="round"/><circle cx="12" cy="22" r="2.2" fill="#222"/><circle cx="23" cy="22" r="2.2" fill="#222"/></svg>
  <div class="abs cart-badge">0</div>
</header>

<section>
  <div class="abs hero" role="img" aria-label="Rain-spotted windshield with a wiper blade over a sunset road"></div>
  <form class="abs finder">
    <h2>SELECT YOUR CAR &amp; SIZE</h2>
    <div class="select first" style="top:81px">Select Make</div>
    <div class="select" style="top:137px">Year</div>
    <div class="select" style="top:194px">Model</div>
    <div class="select" style="top:250px">Wiper Size</div>
    <div class="btn">FIND WIPER FOR MY CAR</div>
    <div class="help">Need Help! <u>Click Here!</u></div>
  </form>
  <h1 class="abs hero-title">BRAVOBLADES<br>SEE IT CLEARLY</h1>
  <div class="btn" style="left:524px;top:423px;width:169px;height:44px">ORDER PARTS</div>
</section>

<section>
  <h2 class="abs head welcome-title">WELCOME<br>TO BRAVO BLADES</h2>
  <div class="abs welcome-copy">
    <p>There's much to see here. So, take your time, look around, and learn all there is to know about us. We hope you enjoy our site and take a moment to drop us a line. Bravo Blades is focused on safety and visibility, our wipers are the best possible solution to help you see while you are driving through heavy rain and snow conditions.</p>
    <p>We are now happy to announce that we are donating a set of Bravo Blades to school busses for every $100 spent this year. When you purchase from us, you are a part of helping bus drivers see clearly world wide.</p>
  </div>
  <div class="btn" style="left:149px;top:1193px;width:168px;height:46px">FIND OUT MORE</div>
  <div class="abs ring"></div>
  <div class="abs ring-photo" role="img" aria-label="Wiper blade clearing a windshield with a city skyline beyond"></div>
</section>

<section>
  <div class="abs wipers" role="img" aria-label="Blurred photo of a man fitting a wiper blade"></div>
  <h2 class="abs head wipers-title">OUR WIPERS</h2>
  <div class="abs wipers-sub">ORDER TWO OR MORE FOR <em>FREE SHIPPING</em></div>

  <svg class="arrow" style="left:86px" width="18" height="30" viewBox="0 0 18 30"><path d="M15 3L4 15l11 12" fill="none" stroke="#fff" stroke-width="3.5"/></svg>
  <svg class="arrow" style="left:1094px" width="18" height="30" viewBox="0 0 18 30"><path d="M3 3l11 12L3 27" fill="none" stroke="#fff" stroke-width="3.5"/></svg>

  <div class="product" style="left:149px">
    <div class="product-photo" role="img" aria-label="Boxed wiper blade on a windshield"></div>
    <div class="product-tag"><div class="name">Soft frameless<br>bracket less rubber</div><div class="meta">24 inches<span class="price">$15.00</span></div></div>
  </div>
  <div class="product" style="left:459px">
    <div class="product-photo" role="img" aria-label="Boxed wiper blade on a windshield"></div>
    <div class="product-tag"><div class="name">Soft frameless<br>bracket less rubber</div><div class="meta">18 inches<span class="price">$14.00</span></div></div>
  </div>
  <div class="product" style="left:767px">
    <div class="product-photo" role="img" aria-label="Boxed wiper blade on a windshield"></div>
    <div class="product-tag"><div class="name">Soft frameless<br>bracket less rubber</div><div class="meta">14 inches<span class="price">$14.00</span></div></div>
  </div>
  <div class="btn" style="left:530px;top:1877px;width:165px;height:44px">ORDER PARTS</div>
</section>

<section>
  <div class="feat-photo" style="left:149px;top:2094px;background:linear-gradient(135deg,#2f3f52 0%,#6f8191 50%,#c9a58c 100%)" role="img" aria-label="Hands fitting a beam wiper blade onto a car"></div>
  <div class="feat-box" style="left:572px;top:2128px;width:477px;height:247px">
    <h3>Did you know?</h3>
    <p>Normal wiper blades should be replaced every six to twelve months?</p>
    <p>Here at Bravo Blades our wipers are designed to hug the curvature of every windshield. We use the beam blade design to provide the best visibility during the rain and snow.</p>
  </div>

  <div class="feat-photo" style="left:534px;top:2488px;height:314px;background:linear-gradient(135deg,#5d7f7f 0%,#c5b49a 45%,#3a4550 100%)" role="img" aria-label="Smiling man replacing a wiper blade on his car"></div>
  <div class="feat-box" style="left:149px;top:2520px;width:478px;height:249px">
    <h3>Silicone or rubber?</h3>
    <p>Silicone is more durable than rubber. Silicone wipers can last twice as long as rubber. Bravo Blades uses a special type of silicone that will not only outlast, but also outperform the competition. It's also designed to have better resistance to the elements and can withstand the hot summers and coldest of winters.</p>
  </div>

  <div class="feat-photo" style="left:149px;top:2880px;height:315px;background:linear-gradient(180deg,#fbfbfb 0%,#eef1f2 100%);box-shadow:0 4px 14px rgba(0,0,0,.08)" role="img" aria-label="Chart of eight common wiper wear problems"></div>
  <div class="feat-box" style="left:572px;top:2914px;width:477px;height:247px">
    <h3>Is it time to replace?</h3>
    <p>If you are experiencing any of these problems, then it is time to replace. We cover rain and snow with these windshield wipers.</p>
    <p>Bravo Blades offers the perfect size blade that is made to specifically fit your vehicle.</p>
  </div>
</section>

<footer>
  <div class="abs footer"></div>
  <svg class="abs" style="left:0;top:3290px" width="1200" height="30" viewBox="0 0 1200 30" preserveAspectRatio="none">
    <path d="M0 17L20 12 45 18 70 9 96 16 130 11 160 18 190 8 220 15 262 10 300 17 335 7 370 14 410 10 450 18 490 9 530 15 570 11 610 17 650 8 690 14 730 10 770 18 810 9 850 15 890 11 930 17 970 7 1010 14 1050 10 1090 18 1130 9 1165 15 1200 11V30H0Z" fill="#4d4d50"/>
  </svg>
  <div class="f-head" style="left:149px">LINKS</div>
  <ul class="f-list" style="left:151px"><li>Home</li><li>Contact Us</li><li>About Us</li><li>Order</li></ul>
  <div class="f-head" style="left:305px">HOURS</div>
  <ul class="f-list" style="left:307px"><li>Monday - Friday: 9am - 5pm</li><li>Saturday: 10am - 4pm</li><li>Sunday: Closed</li></ul>
  <div class="abs divider"></div>
  <div class="f-head" style="left:659px">SUBSCRIBE TO OUR NEWSLETTER</div>
  <div class="abs f-note">Get 10% off your first purchase when you sign up for our yearly reminder.</div>
  <div class="abs email">Email Address</div>
  <div class="btn" style="left:931px;top:3514px;width:116px;height:44px;border-radius:0 5px 5px 0">SIGN UP</div>
  <div class="abs copyright">Copyright © 2023 Bravo Blades - All Rights Reserved.</div>
</footer>

</body>
</html>
```